Criação de Kit Layout de Posts para Redes Sociais (Facebook, Instagram e etc) para Marketing & Comunicação
A empresa queria:
" Produzimos máscara personalizada reutilizável "

```html
<!DOCTYPE html>
<html lang="pt-BR">
<head>
<meta charset="utf-8">
<title>Previna-se – Kit máscaras reutilizáveis</title>
<link rel="stylesheet" href="https://fonts.googleapis.com/css2?family=Permanent+Marker&family=Nothing+You+Could+Do&family=Montserrat:wght@400;500&display=swap">
<style>
  :root {
    --bg: #ececec;
    --teal: #2ba3a6;
    --ink: #3a3a3a;
    --muted: #7c8a8c;
    --mask-pink: #f2c9dc;
    --mask-cream: #f5efd8;
    --mask-sand: #eee3cc;
  }
  html, body {
    margin: 0;
    padding: 0;
    width: 1200px;
    height: 1200px;
    overflow: hidden;
    background: var(--bg);
  }
  .post {
    position: relative;
    width: 1200px;
    height: 1200px;
    background: radial-gradient(circle at 40% 45%, #f4f4f4 0%, var(--bg) 70%);
    overflow: hidden;
  }
  .post__art {
    position: absolute;
    inset: 0;
  }
  .headline {
    position: absolute;
    left: 615px;
    top: 120px;
    width: 530px;
    margin: 0;
    font-family: "Permanent Marker", cursive;
    font-weight: 400;
    font-size: 62px;
    line-height: 1.12;
    color: var(--teal);
    text-align: center;
    white-space: nowrap;
    transform: rotate(-7deg);
    text-shadow: 3px 3px 0 #fff, -2px -2px 0 #fff, 2px -2px 0 #fff, -2px 2px 0 #fff;
  }
  .offer {
    position: absolute;
    left: 670px;
    top: 865px;
    width: 490px;
    margin: 0;
    font-family: "Nothing You Could Do", cursive;
    font-size: 38px;
    line-height: 1.2;
    color: var(--ink);
    text-align: center;
    white-space: nowrap;
    transform: rotate(-6deg);
  }
  .price {
    position: absolute;
    left: 860px;
    top: 985px;
    margin: 0;
    font-family: "Nothing You Could Do", cursive;
    font-size: 78px;
    line-height: 1;
    color: var(--teal);
    transform: rotate(-6deg);
    white-space: nowrap;
  }
  .price__currency {
    font-size: 34px;
    margin-right: 14px;
  }
  .brand {
    position: absolute;
    left: 290px;
    top: 1085px;
    display: flex;
    flex-direction: column;
    align-items: flex-start;
  }
  .brand__name {
    font-family: "Montserrat", sans-serif;
    font-weight: 400;
    font-size: 58px;
    letter-spacing: 2px;
    color: var(--teal);
    line-height: 1;
  }
  .brand__tagline {
    margin-top: 10px;
    font-family: "Montserrat", sans-serif;
    font-weight: 500;
    font-size: 17px;
    letter-spacing: 2px;
    color: var(--muted);
  }
</style>
</head>
<body>
<main class="post">
  <svg class="post__art" width="1200" height="1200" viewBox="0 0 1200 1200">
    <defs>
      <linearGradient id="maskGradient" x1="0" y1="0" x2="1" y2="1">
        <stop offset="0" stop-color="var(--mask-pink)"/>
        <stop offset="0.35" stop-color="var(--mask-cream)"/>
        <stop offset="0.6" stop-color="var(--mask-pink)"/>
        <stop offset="1" stop-color="var(--mask-sand)"/>
      </linearGradient>
    </defs>
    <polyline class="frame-line" points="250,34 1176,34 1176,690" fill="none" stroke="var(--teal)" stroke-width="3"/>
    <polygon class="product-photo" role="img" aria-label="Foto de cinco máscaras de tecido reutilizáveis estampadas, em tons de rosa e creme, empilhadas"
             points="0,50 600,50 640,150 810,520 820,960 160,975 0,830"
             fill="url(#maskGradient)"/>
  </svg>

  <h1 class="headline">PREVINA-SE<br>CONTRA O<br>CORONAVÍRUS</h1>

  <p class="offer">Kit com 5 máscaras<br>reutilizáveis</p>
  <p class="price"><span class="price__currency">R$</span>80,00</p>

  <div class="brand">
    <span class="brand__name">TECIDOVALE</span>
    <span class="brand__tagline">MÁSCARA PERSONALIZADA REUTILIZÁVEL</span>
  </div>
</main>
</body>
</html>
```